Ridgecrest Balusters Website Redesign

I want a fresh new design for my website. Original website
www.ridgecrestbalusters.example. Will need to add additional photos for winning designer. Please use the basic layout for new design. Looking to get a more modern, functional site to attract new customer and ne bale to highlight past projects. Need it to be easy to navigate and get in touch with me for inquiries.

Target Market(s)

Builders and home owners in WA state

Industry/Entity Type

Building, Construction, Deck building

Coding

Coded - Design and coding required

Number of Pages Required

5+ page

Font styles to use
Sans Serif

Colors
0054AA
0677BA
7BADD7
CADEEF
E8F1F8
0094D4
00A9DD
6FCCEA
C7EBF8
E9F6FB
00AB8E
00BBA5
67D7C9
C6EFE9
E9F9F6
59FF00
82FF00
B8FF75
E3FFCB
F4FFEA

Requirements
Must have
• Will need to add more photos of completed projects
Nice to have
• Fresh take on old website, something modern
Should not have
• Nothing comes to mind

```html
<!DOCTYPE html>
<html lang="en">
<head>
<meta charset="utf-8">
<title>Ridgecrest Balusters — Products</title>
<link href="https://fonts.googleapis.com/css2?family=Lato:wght@400;700&display=swap" rel="stylesheet">
<style>
  :root {
    --ink: #111111;
    --blue-tint: #cadeef;
    --green-tint: #f4ffea;
    --sky: #00a9dd;
    --lime: #e3ffcb;
    --lime-mid: #b8ff75;
    --menu-line: #0094d4;
    --brand-green: #1b6b3a;
    --white: #ffffff;
  }
  * { box-sizing: border-box; margin: 0; padding: 0; }
  html, body { width: 1200px; height: 2178px; overflow: hidden; }
  body {
    position: relative;
    font-family: "Lato", Arial, sans-serif;
    color: var(--ink);
    background:
      radial-gradient(ellipse 520px 900px at 270px 1050px, rgba(202,222,239,0.75), rgba(202,222,239,0) 70%),
      radial-gradient(ellipse 520px 900px at 960px 1250px, rgba(227,255,203,0.7), rgba(227,255,203,0) 70%),
      #fbfcfd;
  }
  .float-btn {
    position: absolute; left: 1084px; width: 62px; height: 62px; border-radius: 50%;
    display: flex; align-items: center; justify-content: center;
  }
  .float-btn--mail { top: 32px; background: var(--sky); }
  .float-btn--menu { top: 117px; background: var(--lime); }

  .product-card {
    position: absolute; left: 319px; width: 562px; height: 325px;
    border-radius: 12px; overflow: hidden; display: flex;
  }
  .product-card__photo { width: 281px; height: 100%; }
  .product-card__label {
    width: 281px; height: 100%; display: flex; align-items: center;
    font-weight: 700; font-size: 20px; letter-spacing: -0.2px;
  }
  .product-card--picket .product-card__label { background: var(--blue-tint); padding-left: 31px; }
  .product-card--glass .product-card__label { background: var(--green-tint); padding-left: 51px; }
  .photo--picket { background: linear-gradient(180deg, #8a7a68 0%, #4d4a46 40%, #8b8a86 75%, #a3a29d 100%); }
  .photo--glass { background: linear-gradient(180deg, #3f7fc4 0%, #8fb6de 30%, #5d7d4a 52%, #a5603c 75%, #8c4a2c 100%); }

  .site-footer {
    position: absolute; left: 0; top: 1973px; width: 1200px; height: 205px;
    background: var(--blue-tint);
  }
  .footer-brand {
    position: absolute; left: 46px; top: 56px; width: 93px; height: 93px;
    background: var(--white); display: flex; align-items: center; justify-content: center;
    text-align: center; color: var(--brand-green); font-size: 15px; font-weight: 400; line-height: 1.25;
  }
  .footer-credit { position: absolute; left: 157px; top: 96px; font-size: 10.5px; color: #333; }
  .footer-nav { position: absolute; left: 564px; top: 38px; list-style: none; }
  .footer-nav li { font-size: 11px; font-weight: 700; height: 25px; text-transform: uppercase; letter-spacing: 0.1px; }
  .footer-social { position: absolute; left: 997px; top: 59px; display: flex; gap: 18px; }
  .footer-social span { width: 20px; height: 20px; border-radius: 50%; background: var(--lime-mid); display: block; }
</style>
</head>
<body>
  <a class="float-btn float-btn--mail" aria-label="Email us">
    <svg width="40" height="26" viewBox="0 0 40 26" fill="none" stroke="#fff" stroke-width="3">
      <rect x="2" y="2" width="36" height="22" rx="3"/>
      <path d="M2 3 L20 15 L38 3 M2 23 L15 12 M38 23 L25 12"/>
    </svg>
  </a>
  <a class="float-btn float-btn--menu" aria-label="Open menu">
    <svg width="40" height="26" viewBox="0 0 40 26" stroke="var(--menu-line)" stroke-width="3" stroke-linecap="round">
      <path d="M2 3 H38 M2 13 H38 M2 23 H38"/>
    </svg>
  </a>

  <section class="product-card product-card--picket" style="top:94px">
    <div class="product-card__photo photo--picket" role="img" aria-label="Black vertical picket railing on a covered concrete patio"></div>
    <h2 class="product-card__label">Traditional Vertical Picket</h2>
  </section>
  <section class="product-card product-card--glass" style="top:534px">
    <h2 class="product-card__label">Topless Glass</h2>
    <div class="product-card__photo photo--glass" role="img" aria-label="Topless glass railing on a wood deck overlooking trees"></div>
  </section>
  <section class="product-card product-card--picket" style="top:974px">
    <div class="product-card__photo photo--picket" role="img" aria-label="Black vertical picket railing on a covered concrete patio"></div>
    <h2 class="product-card__label">Traditional Vertical Picket</h2>
  </section>
  <section class="product-card product-card--glass" style="top:1415px">
    <h2 class="product-card__label">Topless Glass</h2>
    <div class="product-card__photo photo--glass" role="img" aria-label="Topless glass railing on a wood deck overlooking trees"></div>
  </section>

  <footer class="site-footer">
    <div class="footer-brand">Ridgecrest<br>Balusters</div>
    <p class="footer-credit">Powered by Larkfield Studio</p>
    <ul class="footer-nav">
      <li>Home</li>
      <li>Products</li>
      <li>About</li>
      <li>Railing Project Pictures</li>
      <li>Remodel Projects</li>
    </ul>
    <div class="footer-social" aria-label="Social links">
      <span></span><span></span><span></span><span></span>
    </div>
  </footer>
</body>
</html>
```